Landing Page für Kornwiese-Prüfset.de
Zielgruppe
Domain: Kornwiese-Prüfset.de
THC Schnelltests mit gringer Anzeigegrenze mit 5ng/ml, ausgerichtet auf die Selbstkontrolle für die Fahrtauglichkeit (Grenze im Gesetz 3,5ng/ml)
Farbe: grün
Anregung siehe Bild
Aufgabenstellung
- Conversionoptimiert
- Soll auf unseren Webshop www.rv-vitalis.de verlinken

```html
<!DOCTYPE html>
<html lang="de">
<head>
<meta charset="utf-8">
<title>Kornwiese-Prüfset.de – Mach den Selbsttest</title>
<link rel="stylesheet" href="https://fonts.googleapis.com/css2?family=Jost:wght@400;500;600;700&display=swap">
<style>
:root{
  --ink:#111111;
  --dark:#131313;
  --paper:#ffffff;
  --card:#f3f3f3;
  --muted:#333333;
  --soft:#9a9a9a;
  --line:#cfcfcf;
  --green:#3a9b4a;
  --star:#e4ef1c;
}
*{box-sizing:border-box;margin:0;padding:0}
html,body{width:1200px;height:2881px;overflow:hidden;background:var(--paper);font-family:"Jost",sans-serif;color:var(--ink)}
.page{position:relative;width:1200px;height:2881px}
.abs{position:absolute}
.pill{display:inline-block;background:#eee;border-radius:12px;font-size:8px;padding:4px 9px;color:var(--ink)}
.btn{display:inline-block;border-radius:6px;font-size:12px;padding:8px 15px;text-decoration:none}
.btn-dark{background:var(--ink);color:#fff}
.btn-light{background:#fff;color:var(--ink)}

/* hero */
.hero{left:0;top:0;width:1200px;height:525px;border-radius:0 0 18px 18px;overflow:hidden;
  background:radial-gradient(ellipse at 70% 35%,#c9a57a 0%,#8a5a30 35%,#3d2414 70%,#1a0f08 100%)}
.nav{left:125px;top:38px;width:950px;height:66px;border-radius:8px;background:rgba(255,255,255,.08);display:flex;align-items:center;padding:0 24px 0 25px}
.nav .logo{color:#fff;font-weight:600;font-size:20px;letter-spacing:-.2px;flex:1}
.nav a{color:#fff;font-size:12px;text-decoration:none;margin-left:24px}
.nav a.active{background:#fff;color:var(--ink);padding:6px 15px;border-radius:6px;margin-left:0}
.nav a.btn-dark{padding:8px 15px;margin-left:32px}
.hero-copy{left:155px;top:292px;color:#fff}
.hero-copy h1{font-size:40px;font-weight:700;margin-top:6px;letter-spacing:-.3px}
.hero-copy p{font-size:15px;margin:2px 0 18px}
.badge{left:1057px;top:473px;width:128px;height:36px;border-radius:6px;background:#fff;display:flex;align-items:center;padding-left:10px;gap:8px}
.badge i{width:24px;height:24px;border-radius:50%;background:#2c4f8a}
.badge b{width:78px;height:12px;border-radius:3px;background:#ddd}

/* features */
.feature{top:572px;width:320px;text-align:center}
.feature svg{height:40px}
.feature h3{font-size:20px;font-weight:500;margin-top:8px}
.feature p{font-size:12.5px;line-height:20px;color:var(--muted)}

/* problem */
.problem{left:155px;top:773px}
.problem h2,.center-head h2{font-size:20px;font-weight:500;margin-top:7px;letter-spacing:.1px}
.problem p.sub,.center-head p{font-size:13.5px}
.u{text-decoration:underline;text-decoration-color:var(--green);text-underline-offset:3px}
.reason{left:199px;width:802px;height:130px;background:var(--card);border-radius:10px;border-right:10px solid var(--ink);display:flex;align-items:center}
.reason .num{width:84px;text-align:center;font-size:66px;font-weight:500}
.reason h4{font-size:15.5px;font-weight:500;margin-bottom:8px}
.reason p{font-size:13.5px;line-height:20px;color:var(--muted);padding-right:20px}

/* testimonials */
.reviews{left:0;top:1503px;width:1200px;height:723px;background:var(--dark);color:#fff}
.center-head{width:1200px;text-align:center}
.reviews .center-head{top:68px}
.col{top:0;width:310px}
.review{background:#fff;color:var(--ink);border-radius:10px;padding:16px 21px 18px;margin-bottom:30px;position:relative}
.stars{display:flex;gap:13px;height:22px}
.stars svg{width:22px;height:22px}
.g{position:absolute;right:16px;top:17px;width:22px;height:22px;border-radius:50%;border:4px solid #e04a3a}
.review h5{font-size:12.5px;font-weight:500;margin:12px 0 12px}
.review p{font-size:13.5px;line-height:20px;color:var(--muted)}
.review small{display:block;font-size:10px;font-weight:500;margin-top:14px}

/* faq */
.faq{left:125px;top:2394px;width:950px;border-top:1px solid var(--line)}
.faq div{height:58px;border-bottom:1px solid var(--line);display:flex;align-items:center;justify-content:space-between;padding:0 10px 0 17px;font-size:12px;font-weight:500}

.footer{left:0;top:2748px;width:1200px;text-align:center}
.footer .brand{font-size:22px;font-weight:700;display:inline-flex;align-items:center;gap:8px}
.footer .brand i{width:14px;height:14px;background:var(--ink)}
.footer .links{font-size:13.5px;margin-top:16px;color:var(--muted)}
.footer .copy{font-size:13px;color:#c4c4c4;margin-top:14px}
</style>
</head>
<body>
<div class="page">

  <section class="abs hero" role="img" aria-label="Foto: Person am Steuer eines Autos, Blick durch die Windschutzscheibe in warmem Gegenlicht"></section>
  <nav class="abs nav">
    <span class="logo">KORNWIESE-PRÜFSET.DE</span>
    <a class="active" href="#">Start</a>
    <a href="#">Unsere Lösung</a>
    <a href="#">FAQ</a>
    <a class="btn btn-dark" href="https://www.rv-vitalis.de">Jetzt kaufen</a>
  </nav>
  <div class="abs hero-copy">
    <span class="pill">THC-Schnelltest</span>
    <h1>MACH DEN SELBSTTEST.</h1>
    <p>Gefährde nicht deinen Führerschein!</p>
    <a class="btn btn-light" href="https://www.rv-vitalis.de">Jetzt kaufen</a>
  </div>
  <div class="abs badge" aria-label="Zertifikat"><i></i><b></b></div>

  <div class="abs feature" style="left:113px">
    <svg viewBox="0 0 24 24" width="40"><path d="M13 2 4 14h7l-1 8 9-12h-7z" fill="#111"/></svg>
    <h3>SCHNELL</h3>
    <p>Ergebnisse in wenigen Minuten sofortige<br>Sicherheit für Ihre Fahrtüchtigkeit.</p>
  </div>
  <div class="abs feature" style="left:440px">
    <svg viewBox="0 0 24 24" width="40" fill="none" stroke="#111" stroke-width="2"><path d="M12 2v5M12 17v5M2 12h5M17 12h5"/><circle cx="12" cy="12" r="1.5" fill="#111"/></svg>
    <h3>PRÄZISE</h3>
    <p>Genaue Messung mit einer Anzeigegrenze<br>von 5ng/ml für verlässliche Ergebnisse.</p>
  </div>
  <div class="abs feature" style="left:760px">
    <svg viewBox="0 0 24 24" width="40"><path d="M2 10h4v11H2zM8 21V10l5-8c2 0 3 1 2.5 3L14 9h6c1.5 0 2.5 1.3 2 2.8l-2.5 7.5c-.4 1-1.2 1.7-2.3 1.7z" fill="#111"/></svg>
    <h3>EINFACH</h3>
    <p>Einfache Anwendung, die jeder<br>problemlos zu Hause durchführen kann.</p>
  </div>

  <div class="abs problem">
    <span class="pill">Das Problem</span>
    <h2>DIE GRENZE FÜR THC IM BLUT WÄHREND DER FAHRT BETRÄGT <span class="u">3.5NG/ML</span></h2>
    <p class="sub">Sind Sie sicher, dass Sie darunter liegen? 3 Gründe die für einen Schnelltest sprechen:</p>
  </div>

  <div class="abs reason" style="top:882px">
    <div class="num">1</div>
    <div><h4>INDIVIDUELLE UNTERSCHIEDE IM STOFFWECHSEL</h4>
    <p>Jeder Mensch baut THC unterschiedlich schnell ab. Faktoren wie Körpergewicht, Stoffwechselrate und genetische Disposition können die THC-Konzentration im Blut beeinflussen. Was für den einen sicher ist, könnte für den anderen problematisch sein.</p></div>
  </div>
  <div class="abs reason" style="top:1042px">
    <div class="num">2</div>
    <div><h4>LANGFRISTIGE SPEICHERUNG VON THC</h4>
    <p>THC kann sich im Fettgewebe ansammeln und langsam wieder freigesetzt werden, auch Tage nach dem Konsum. Dies bedeutet, dass selbst wenn Sie sich nicht berauscht fühlen, noch THC in Ihrem Blutkreislauf vorhanden sein kann und Sie über dem gesetzlichen Grenzwert liegen.</p></div>
  </div>
  <div class="abs reason" style="top:1202px">
    <div class="num">3</div>
    <div><h4>REGELMÄẞIGER KONSUM UND SEINE AUSWIRKUNGEN</h4>
    <p>Regelmäßige Konsumenten entwickeln oft eine Toleranz gegenüber den psychoaktiven Effekten von THC, was dazu führen kann, dass sie ihre Fahrtüchtigkeit überschätzen. Auch wenn man sich nüchtern fühlt, können die Blutwerte über dem Grenzwert liegen und zu rechtlichen Konsequenzen führen.</p></div>
  </div>
  <div class="abs" style="left:0;top:1362px;width:1200px;text-align:center"><a class="btn btn-dark" href="https://www.rv-vitalis.de">Jetzt Schnelltest bestellen</a></div>

  <section class="abs reviews">
    <div class="abs center-head">
      <span class="pill">Testimoials</span>
      <h2>ERFAHRUNGEN UNSERER KUNDEN – VERTRAUEN SIE AUF DEN <span class="u">KORNWIESE-PRÜFSET</span></h2>
      <p>Sind Sie sicher, dass Sie darunter liegen? 3 Gründe die für einen Schnelltest sprechen:</p>
    </div>
    <svg width="0" height="0" style="position:absolute"><defs><path id="star" d="M12 1.5l3.2 6.9 7.3.8-5.4 5 1.5 7.3L12 17.8l-6.6 3.7 1.5-7.3-5.4-5 7.3-.8z" fill="#e4ef1c"/></defs></svg>

    <div class="abs col" style="left:107px;top:176px">
      <div class="review"><div class="stars"><svg viewBox="0 0 24 24"><use href="#star"/></svg><svg viewBox="0 0 24 24"><use href="#star"/></svg><svg viewBox="0 0 24 24"><use href="#star"/></svg><svg viewBox="0 0 24 24"><use href="#star"/></svg><svg viewBox="0 0 24 24"><use href="#star"/></svg></div><i class="g"></i>
        <h5>BEEINDRUCKENDE GENAUIGKEIT</h5><p>Ich habe den Kornwiese-Prüfset verwendet und war beeindruckt von der Genauigkeit und Einfachheit. Jetzt fühle ich mich sicher, bevor ich ins Auto steige.</p><small>JONAS MEHRFELD - 22. JULI 2024</small></div>
      <div class="review"><div class="stars"><svg viewBox="0 0 24 24"><use href="#star"/></svg><svg viewBox="0 0 24 24"><use href="#star"/></svg><svg viewBox="0 0 24 24"><use href="#star"/></svg><svg viewBox="0 0 24 24"><use href="#star"/></svg></div><i class="g"></i>
        <h5>VERLÄSSLICHER TEST</h5><p>Endlich ein Test, dem ich vertrauen kann. Der Kornwiese-Prüfset gibt mir die Gewissheit, die ich brauche.</p><small>LENA HAINBACH - 24. JULI 2024</small></div>
    </div>
    <div class="abs col" style="left:445px;top:203px">
      <div class="review"><div class="stars"><svg viewBox="0 0 24 24"><use href="#star"/></svg><svg viewBox="0 0 24 24"><use href="#star"/></svg><svg viewBox="0 0 24 24"><use href="#star"/></svg><svg viewBox="0 0 24 24"><use href="#star"/></svg></div><i class="g"></i>
        <h5>VERLÄSSLICHER TEST</h5><p>Endlich ein Test, dem ich vertrauen kann. Der Kornwiese-Prüfset gibt mir die Gewissheit, die ich brauche.</p><small>LENA HAINBACH - 24. JULI 2024</small></div>
      <div class="review"><div class="stars"><svg viewBox="0 0 24 24"><use href="#star"/></svg><svg viewBox="0 0 24 24"><use href="#star"/></svg><svg viewBox="0 0 24 24"><use href="#star"/></svg><svg viewBox="0 0 24 24"><use href="#star"/></svg><svg viewBox="0 0 24 24"><use href="#star"/></svg></div><i class="g"></i>
        <h5>BEEINDRUCKENDE GENAUIGKEIT</h5><p>Ich habe den Kornwiese-Prüfset verwendet und war beeindruckt von der Genauigkeit und Einfachheit. Jetzt fühle ich mich sicher, bevor ich ins Auto steige.</p><small>JONAS MEHRFELD - 22. JULI 2024</small></div>
    </div>
    <div class="abs col" style="left:783px;top:238px">
      <div class="review"><div class="stars"><svg viewBox="0 0 24 24"><use href="#star"/></svg><svg viewBox="0 0 24 24"><use href="#star"/></svg><svg viewBox="0 0 24 24"><use href="#star"/></svg><svg viewBox="0 0 24 24"><use href="#star"/></svg></div><i class="g"></i>
        <h5>SCHNELLE ERGEBNISSE</h5><p>Schnelle und präzise Ergebnisse, die mir helfen, sicher auf den Straßen unterwegs zu sein. Sehr empfehlenswert!</p><small>TOBIAS WENDLER - 02. APRIL 2024</small></div>
      <div class="review"><div class="stars"><svg viewBox="0 0 24 24"><use href="#star"/></svg><svg viewBox="0 0 24 24"><use href="#star"/></svg><svg viewBox="0 0 24 24"><use href="#star"/></svg><svg viewBox="0 0 24 24"><use href="#star"/></svg></div><i class="g"></i>
        <h5>SCHNELLE ERGEBNISSE</h5><p>Schnelle und präzise Ergebnisse, die mir helfen, sicher auf den Straßen unterwegs zu sein. Sehr empfehlenswert!</p><small>TOBIAS WENDLER - 02. APRIL 2024</small></div>
    </div>
  </section>

  <div class="abs center-head" style="left:0;top:2313px">
    <span class="pill">FAQ</span>
    <h2>HÄUFIG GESTELLTE FRAGEN</h2>
  </div>
  <div class="abs faq">
    <div>Lorem ipsum dolor sit amet, consetetur sadipscing elitr<svg width="12" height="16" viewBox="0 0 12 16"><path d="M3 2l6 6-6 6" fill="none" stroke="#111" stroke-width="2"/></svg></div>
    <div>diam nonumy eirmod tempor invidunt<svg width="12" height="16" viewBox="0 0 12 16"><path d="M3 2l6 6-6 6" fill="none" stroke="#111" stroke-width="2"/></svg></div>
    <div>At vero eos et accusam et justo duo dolores et ea rebum. Stet clita kasd gubergren<svg width="12" height="16" viewBox="0 0 12 16"><path d="M3 2l6 6-6 6" fill="none" stroke="#111" stroke-width="2"/></svg></div>
    <div>Lorem ipsum dolor sit amet. Lorem ipsum dolor sit amet, consetetur sadipscing elitr, sed diam nonumy eirmod<svg width="12" height="16" viewBox="0 0 12 16"><path d="M3 2l6 6-6 6" fill="none" stroke="#111" stroke-width="2"/></svg></div>
  </div>
  <div class="abs" style="left:0;top:2660px;width:1200px;text-align:center"><a class="btn btn-dark" href="https://www.rv-vitalis.de">Jetzt Schnelltest bestellen</a></div>

  <footer class="abs footer">
    <a class="brand" href="https://www.rv-vitalis.de" style="color:inherit;text-decoration:none"><i></i>RV VITALIS</a>
    <p class="links">Impressum / Datenschutz / AGB</p>
    <p class="copy">©2024 R &amp; V Handel GbR</p>
  </footer>
</div>
</body>
</html>
```